Letterhead and compliment slip

We are a UK-based market research agency. We are looking for a new letterhead design to incorporate our logo, address details and company information. We are looking for a simple design. It should be modern. It needs to have a qualify feel. As we are UK based it needs to be designed for A4 paper size (letterhead).
I'm really looking for something simple in design terms!
Both letterhead and compliment slip need to include:
Our logo
Company address
Telephone number
Email address
Website address
Company registration number
VAT registration number
Grey and green would be a good colour scheme to fit with our logo

```html
<!DOCTYPE html>
<html lang="en">
<head>
<meta charset="utf-8">
<title>Brightline Consumer Research – Letterhead</title>
<link href="https://fonts.googleapis.com/css2?family=Open+Sans:wght@400;600;700&display=swap" rel="stylesheet">
<style>
  :root{
    --green:#5fae46;
    --ink:#2b2b2b;
    --body:#3a3a3a;
    --icon:#8a8a8a;
    --paper:#ffffff;
  }
  *{box-sizing:border-box;margin:0;padding:0}
  html,body{width:851px;height:1200px;overflow:hidden;background:var(--paper)}
  .letterhead{position:relative;width:851px;height:1200px;font-family:"Open Sans",Arial,sans-serif;color:var(--ink)}

  .brand{position:absolute;left:22px;top:30px;display:flex;align-items:center;gap:12px}
  .brand-mark{width:16px;height:16px;background:var(--green)}
  .brand-name{font-size:32px;font-weight:600;color:var(--ink);line-height:1}

  .sidebar{position:absolute;left:54px;width:230px;font-size:10px;line-height:14px;color:var(--ink)}
  .address{top:206px}
  .address .company{font-weight:600}
  .phone{top:348px}
  .email-web{top:433px}
  .contact-icon{display:block;width:14px;height:14px;margin-bottom:12px}

  .letter{position:absolute;left:340px;top:168px;width:384px;font-size:12px;line-height:17px}
  .recipient{font-weight:700}
  .attention{font-weight:700;margin-top:26px}
  .subject{font-weight:700;margin-top:17px}
  .subject span{text-decoration:underline}
  .salutation{font-weight:700;margin-top:20px}
  .body-text{margin-top:102px;color:var(--body)}
  .body-text p+p{margin-top:17px}

  .signoff{position:absolute;left:340px;top:1002px;font-size:12px;line-height:17px;font-weight:700}

  .footer{position:absolute;left:0;bottom:0;width:851px;height:40px;background:var(--green);color:#fff;
    font-size:10.5px;display:flex;align-items:center;justify-content:center;gap:40px}
</style>
</head>
<body>
<div class="letterhead">
  <div class="brand">
    <div class="brand-mark"></div>
    <div class="brand-name">Brightline</div>
  </div>

  <div class="sidebar address">
    <div class="company">Brightline Consumer Research Ltd</div>
    <div>12 Willow House</div>
    <div>Meadowgate</div>
    <div>Oakfield Park</div>
    <div>Harpley</div>
    <div>Westshire</div>
    <div>HP4 2RN</div>
  </div>

  <div class="sidebar phone">
    <svg class="contact-icon" viewBox="0 0 24 24"><circle cx="12" cy="12" r="11" fill="none" stroke="#8a8a8a" stroke-width="1.5"/><path d="M8.5 6.5l2 2-1.2 1.6a7 7 0 0 0 4.6 4.6l1.6-1.2 2 2-1.3 1.5c-4.3.2-9.4-4.9-9.2-9.2z" fill="#8a8a8a"/></svg>
    <div>+44 (0)1632 960 418</div>
  </div>

  <div class="sidebar email-web">
    <svg class="contact-icon" viewBox="0 0 24 24"><circle cx="12" cy="12" r="11" fill="none" stroke="#8a8a8a" stroke-width="1.5"/><rect x="6.5" y="8" width="11" height="8" fill="none" stroke="#8a8a8a" stroke-width="1.4"/><path d="M6.5 8l5.5 4.5L17.5 8" fill="none" stroke="#8a8a8a" stroke-width="1.4"/></svg>
    <div>hello@brightlineresearch.co.uk</div>
    <div>www.brightlineresearch.co.uk</div>
  </div>

  <div class="letter">
    <div class="recipient">
      <div>Marlo</div>
      <div>Blk 18 Kestrel Polytechnic</div>
      <div>The Workshop, #02-07,09</div>
      <div>3 February 2019</div>
    </div>
    <div class="attention">Attention Daniel Wong</div>
    <div class="subject"><span>RE: Enquiry regarding bulk purchase</span></div>
    <div class="salutation">Dear Sir,</div>
    <div class="body-text">
      <p>Lorem ipsum dolor sit amet, consectetur adipiscing elit, sed do eiusmod tempor incididunt ut labore et dolore magna aliqua. Cursus euismod quis viverra nibh. Arcu vitae elementum curabitur vitae nunc sed velit. Facilisi morbi tempus iaculis urna id volutpat lacus laoreet. Dui id ornare arcu odio ut sem nulla. In mollis nunc sed id semper risus in hendrerit gravida. Sodales ut eu sem integer vitae. Hac habitasse platea dictumst vestibulum rhoncus. Sagittis vitae et leo duis ut diam quam nulla. Elit sed vulputate mi sit amet mauris. A erat nam at lectus. Urna neque viverra justo nec ultrices dui sapien. Fermentum odio eu feugiat pretium nibh ipsum. Nunc sed blandit libero volutpat sed cras ornare arcu. In metus vulputate eu scelerisque felis imperdiet proin fermentum. Dictum non consectetur a erat.</p>
      <p>Nisl condimentum id venenatis a condimentum vitae sapien. Molestie ac feugiat sed lectus. Ornare quam viverra orci sagittis eu volutpat odio facilisis. Rhoncus est pellentesque elit ullamcorper dignissim cras tincidunt. Risus commodo viverra maecenas accumsan lacus vel. Convallis aenean et tortor at risus. In fermentum et sollicitudin ac orci. Ac turpis egestas maecenas pharetra convallis posuere. Laoreet sit amet cursus sit amet dictum. Id diam maecenas ultricies mi eget mauris pharetra et. Mauris nunc congue nisi vitae suscipit tellus mauris a. Arcu vitae elementum curabitur vitae nunc. Eget felis eget nunc lobortis. Erat nam at lectus urna duis.</p>
    </div>
  </div>

  <div class="signoff">
    <div>Peter Lim</div>
    <div>Managing Director &amp; Co-founder</div>
  </div>

  <div class="footer">
    <span>Company registration number 7741026</span>
    <span>VAT registration number 305662918</span>
  </div>
</div>
</body>
</html>
```